Company profile infograph to describe key facts about a company

We need to design an infograph.
The Idea of the infograph is to describe a company in one sheet. Company name, company address, financials, recent changes and other data related to the company.
I have attached a brief. The first slide is what the design currently looks, the 3 second slides are how it should look. Please be creative and take ideas from other infographs! The main idea is that when a person sees the infograph, the first impression is that she understands what's up with the company.
Industry/Entity Type
It Company
Number of Pages Required
1 page
Font styles to use
Other font styles liked:
- Avenir Next
Look and feel
Each slider illustrates characteristics of the customer's brand and the style your logo design should communicate.

```html
<!DOCTYPE html>
<html lang="en">
<head>
<meta charset="utf-8">
<title>norvik – Company Profile</title>
<link href="https://fonts.googleapis.com/css2?family=Open+Sans:wght@400;600;700&display=swap" rel="stylesheet">
<style>
  :root {
    --bg: #f5f5f5;
    --navy: #1f5a9c;
    --sky: #3aa6dc;
    --green: #8dc63f;
    --lime-hl: #c5e3a0;
    --panel-blue: #4f93cb;
    --panel-grey: #e2e2e2;
    --bar-blue: #3a9ee0;
    --bar-dark: #23466f;
    --bar-green: #9cc54a;
    --text-dark: #222;
    --grey-logo: #a8a8a8;
    --white: #fff;
  }
  html, body { margin: 0; padding: 0; overflow: hidden; }
  body { width: 1032px; height: 1200px; background: var(--bg); font-family: "Open Sans", Arial, sans-serif; }
  .sheet { position: relative; width: 960px; height: 1116px; transform: scale(1.075); transform-origin: 0 0; }
  .abs { position: absolute; }

  .brand { left: 40px; top: 68px; display: flex; align-items: center; gap: 16px; }
  .brand-dot { width: 62px; height: 62px; border-radius: 50%; background: var(--panel-blue); }
  .brand-name { font-size: 58px; font-weight: 400; color: var(--grey-logo); letter-spacing: 1px; line-height: 1; }

  .highlights { left: 348px; top: 24px; margin: 0; padding: 0; list-style: none; }
  .highlights li { margin-bottom: 8px; }
  .highlights span { background: var(--lime-hl); color: var(--navy); font-size: 27px; font-weight: 600; padding: 0 12px 0 10px; line-height: 32px; display: inline-block; }

  .finance { left: 5px; top: 232px; width: 509px; height: 516px; background: var(--panel-grey); }
  .finance-head { height: 100px; background: var(--panel-blue); display: flex; align-items: center; gap: 30px; padding-left: 44px; color: var(--white); font-size: 29px; font-weight: 600; }
  .finance-caption { margin: 12px 0 0 56px; font-size: 14px; color: #444; }
  .revenue-chart { position: absolute; left: 0; top: 200px; }
  .fin-table { position: absolute; left: 64px; top: 335px; border-collapse: collapse; font-size: 14px; color: var(--text-dark); }
  .fin-table th { font-size: 15px; font-weight: 700; padding: 0 6px 8px 0; text-align: left; width: 84px; }
  .fin-table td { text-align: right; padding: 4px 28px 6px 0; }

  .timeline-line { left: 569px; top: 230px; width: 4px; height: 565px; background: var(--green); }
  .event { left: 536px; width: 414px; }
  .event-badge { position: absolute; left: 0; top: 0; width: 70px; height: 70px; border-radius: 50%; background: var(--green); display: flex; align-items: center; justify-content: center; }
  .event-rule { position: absolute; left: 60px; top: 56px; width: 354px; height: 4px; background: var(--green); }
  .event-title { position: absolute; left: 84px; top: 16px; margin: 0; font-size: 23px; font-weight: 600; color: var(--navy); white-space: nowrap; letter-spacing: .3px; }
  .event-note { position: absolute; left: 90px; top: 76px; margin: 0; font-size: 17px; font-weight: 600; color: var(--sky); white-space: nowrap; }
  .event-note::before { content: ""; display: inline-block; border-left: 9px solid var(--sky); border-top: 6px solid transparent; border-bottom: 6px solid transparent; margin-right: 12px; }

  .tech-title { left: 27px; top: 804px; margin: 0; font-size: 29px; font-weight: 600; color: var(--navy); }
  .tech { text-align: center; }
  .tech-label { font-size: 17px; font-weight: 600; color: var(--sky); margin: 0 0 10px; }
  .tech-badge { width: 120px; height: 120px; border-radius: 50%; background: var(--white); border: 1px solid #e4e4e4; display: flex; align-items: center; justify-content: center; margin: 0 auto; font-size: 17px; font-weight: 600; color: var(--navy); }
  .social-row { display: flex; gap: 22px; }
  .social-badge { width: 76px; height: 76px; border-radius: 50%; background: var(--white); border: 1px solid #e4e4e4; display: flex; align-items: center; justify-content: center; font-size: 13px; font-weight: 600; color: var(--navy); }
</style>
</head>
<body>
<div class="sheet">

  <div class="abs brand"><span class="brand-dot"></span><span class="brand-name">norvik</span></div>

  <ul class="abs highlights">
    <li><span>Focuses on digital business</span></li>
    <li><span>Lot of changes recently</span></li>
    <li><span>Performs lower than average in indutry</span></li>
  </ul>

  <section class="abs finance">
    <div class="finance-head">
      <svg width="58" height="44" viewBox="0 0 58 44" aria-hidden="true">
        <path d="M3 2 V41 H56" fill="none" stroke="#fff" stroke-width="4"/>
        <rect x="10" y="20" width="7" height="16" fill="#fff"/>
        <rect x="21" y="10" width="7" height="26" fill="#fff"/>
        <rect x="32" y="16" width="7" height="20" fill="#fff"/>
        <rect x="43" y="26" width="7" height="10" fill="#fff"/>
      </svg>
      Basic Financial Info
    </div>
    <p class="finance-caption">Liikevaihdon kehitys</p>
    <svg class="revenue-chart" width="509" height="120" viewBox="0 0 509 120" aria-label="Revenue development bar chart">
      <g fill="var(--bar-dark)">
        <rect x="68" y="104" width="4" height="8"/><rect x="80" y="103" width="4" height="9"/><rect x="92" y="102" width="4" height="10"/>
      </g>
      <g fill="var(--bar-blue)">
        <rect x="104" y="100" width="4" height="12"/><rect x="116" y="96" width="4" height="16"/><rect x="128" y="92" width="4" height="20"/>
        <rect x="140" y="91" width="4" height="21"/><rect x="152" y="93" width="4" height="19"/><rect x="164" y="95" width="4" height="17"/>
        <rect x="176" y="93" width="4" height="19"/><rect x="188" y="88" width="4" height="24"/><rect x="200" y="80" width="4" height="32"/>
        <rect x="212" y="76" width="4" height="36"/><rect x="224" y="70" width="4" height="42"/><rect x="236" y="62" width="4" height="50"/>
        <rect x="248" y="52" width="4" height="60"/><rect x="260" y="44" width="4" height="68"/><rect x="272" y="36" width="4" height="76"/>
        <rect x="284" y="28" width="4" height="84"/><rect x="296" y="25" width="4" height="87"/><rect x="308" y="32" width="4" height="80"/>
        <rect x="320" y="44" width="4" height="68"/><rect x="332" y="56" width="4" height="56"/><rect x="344" y="62" width="4" height="50"/>
        <rect x="356" y="60" width="4" height="52"/><rect x="368" y="68" width="4" height="44"/><rect x="380" y="64" width="4" height="48"/>
        <rect x="392" y="82" width="4" height="30"/><rect x="404" y="88" width="4" height="24"/><rect x="416" y="96" width="4" height="16"/>
        <rect x="428" y="106" width="4" height="6"/>
      </g>
      <g fill="var(--bar-green)">
        <rect x="224" y="54" width="4" height="13"/><rect x="236" y="46" width="4" height="13"/><rect x="248" y="42" width="4" height="8"/>
        <rect x="356" y="52" width="4" height="6"/><rect x="368" y="52" width="4" height="13"/>
      </g>
    </svg>
    <table class="fin-table">
      <tr><th>2010/09</th><th>2011/09</th><th>2012/12</th><th>2013/12</th><th>2014/12</th></tr>
      <tr><td>6457</td><td>5480</td><td>7469</td><td>5077</td><td>5768</td></tr>
      <tr><td>103.10</td><td>-15.10</td><td>9.00</td><td>-15.00</td><td>13.60</td></tr>
      <tr><td>109</td><td>10</td><td>-94</td><td>56</td><td>70</td></tr>
      <tr><td>1.90</td><td>1.20</td><td>-1.40</td><td>2.30</td><td>6.60</td></tr>
      <tr><td>70</td><td>69</td><td>69</td><td>64</td><td>61</td></tr>
    </table>
  </section>

  <div class="abs timeline-line"></div>

  <article class="abs event" style="top:284px">
    <div class="event-rule"></div>
    <div class="event-badge">
      <svg width="30" height="34" viewBox="0 0 30 34" aria-hidden="true"><circle cx="15" cy="9" r="8" fill="var(--navy)"/><path d="M1 34 C1 22 8 19 15 19 C22 19 29 22 29 34 Z" fill="var(--navy)"/></svg>
    </div>
    <h3 class="event-title">CHANGES IN MANAGEMENT</h3>
    <p class="event-note">Elina And new worker</p>
  </article>

  <article class="abs event" style="top:455px">
    <div class="event-rule"></div>
    <div class="event-badge">
      <svg width="40" height="34" viewBox="0 0 40 34" aria-hidden="true" fill="var(--navy)"><rect x="14" y="0" width="12" height="9"/><rect x="19" y="9" width="2" height="6"/><rect x="4" y="14" width="32" height="2"/><rect x="4" y="14" width="2" height="8"/><rect x="19" y="14" width="2" height="8"/><rect x="34" y="14" width="2" height="8"/><rect x="0" y="22" width="10" height="9"/><rect x="15" y="22" width="10" height="9"/><rect x="30" y="22" width="10" height="9"/></svg>
    </div>
    <h3 class="event-title">ORGANISATIONAL CHANGES</h3>
    <p class="event-note" style="left:100px">New structure in company</p>
  </article>

  <article class="abs event" style="top:625px">
    <div class="event-rule"></div>
    <div class="event-badge">
      <svg width="36" height="34" viewBox="0 0 36 34" aria-hidden="true" fill="var(--navy)"><path d="M18 0 L36 8 V11 H0 V8 Z"/><rect x="4" y="13" width="5" height="14"/><rect x="12" y="13" width="5" height="14"/><rect x="20" y="13" width="5" height="14"/><rect x="28" y="13" width="5" height="14"/><rect x="0" y="29" width="36" height="5"/></svg>
    </div>
    <h3 class="event-title">INVESTMENTS M &amp; A</h3>
    <p class="event-note" style="left:96px">Company buy its competitor</p>
  </article>

  <h2 class="abs tech-title">Used Technologies</h2>

  <div class="abs tech" style="left:25px;top:858px;width:120px">
    <p class="tech-label" style="text-align:left;margin-left:4px">MARKETING</p>
    <div class="tech-badge">Adreach</div>
  </div>
  <div class="abs tech" style="left:283px;top:858px;width:122px">
    <p class="tech-label">E-COMMERCE</p>
    <div class="tech-badge">Shopforge</div>
  </div>
  <div class="abs tech" style="left:541px;top:858px;width:122px">
    <p class="tech-label">WEBPAGE</p>
    <div class="tech-badge">Pagecraft</div>
  </div>
  <div class="abs tech" style="left:768px;top:858px;width:175px">
    <p class="tech-label" style="text-align:right">SOCIAL MEDIA</p>
    <div class="social-row" style="margin-top:20px">
      <div class="social-badge">Friendly</div>
      <div class="social-badge">Chirper</div>
    </div>
  </div>

</div>
</body>
</html>
```